hotel's Website

Hotels website redesign for reference pictures, logo etc see http://restwellmarlow.co.uk/

1. 2-3 Special offers on the main page.
2. Booking calender
3. Location Map
4. Picture gallery.
5. Journeyscope reviews.
6. short description
7. Social Media sharing.
8 Phone number and address.

Industry/Entity Type

Hotel

Requirements
Must have
• 1. 2-3 Special offers on the main page.
2. Booking calender
3. Location Map
4. Picture gallery.
5. Journeyscope reviews.
6. short description
7. Social Media sharing.

```html
<!DOCTYPE html>
<html lang="en">
<head>
<meta charset="utf-8">
<title>Restwell Inn - London Victoria</title>
<link href="https://fonts.googleapis.com/css2?family=Bitter:wght@400;700&family=Roboto:wght@400;500;700&family=Roboto+Condensed:wght@400;700&display=swap" rel="stylesheet">
<style>
:root{
  --wood:#5a2a14;
  --blue:#0b5fb5;
  --yellow:#ffe21a;
  --yellow-dark:#e6c800;
  --text:#555;
  --heading:#333;
  --red:#e0141e;
  --line:#ddd;
  --white:#fff;
  --bullet:#f2b600;
}
*{margin:0;padding:0;box-sizing:border-box}
html,body{width:1059px;height:1200px;overflow:hidden}
body{position:relative;font-family:'Bitter',serif;color:var(--text);
  background:linear-gradient(180deg,var(--wood) 0,#4a2110 250px,#2a1108 430px,#0a0503 560px,#000 700px,#000 100%)}
.abs{position:absolute}
.topbar{right:116px;top:8px;text-align:right;font-family:'Roboto',sans-serif;color:var(--white);font-weight:700}
.translate{font-size:10px;display:flex;align-items:center;justify-content:flex-end;gap:4px}
.lang{background:#eee;color:#333;font-weight:400;font-size:10px;width:99px;height:21px;border:1px solid #bbb;display:flex;align-items:center;padding:0 6px;gap:6px}
.lang .flag{width:16px;height:11px;background:#2a4c9a}
.lang .caret{margin-left:auto;border:4px solid transparent;border-top:5px solid #333;margin-top:4px}
.phone{font-size:13px;margin-top:5px;display:flex;align-items:center;justify-content:flex-end;gap:5px}
.email{font-size:9.5px;margin-top:4px;display:flex;align-items:center;justify-content:flex-end;gap:5px}
.panel{left:117px;top:73px;width:826px;height:1093px;background:var(--white);border-radius:8px}
.nav{left:132px;top:93px;width:795px;height:42px;background:var(--blue);display:flex;align-items:center}
.nav .home{width:48px;height:42px;background:var(--yellow);display:flex;align-items:center;justify-content:center}
.nav a{color:var(--white);text-decoration:none;font-size:10px;letter-spacing:.6px;text-transform:uppercase}
.nav .left{display:flex;gap:25px;margin-left:16px}
.nav .right{display:flex;gap:25px;margin-left:auto;margin-right:18px}
.logo{left:480px;top:41px;width:103px;height:114px;background:var(--white);text-align:center;font-family:'Bitter',serif;display:flex;flex-direction:column;align-items:center}
.logo .loc{font-size:6.5px;color:var(--blue);font-weight:700;margin-top:4px;letter-spacing:.3px}
.logo .square{width:34px;height:34px;background:var(--blue);margin-top:10px}
.logo .name{color:var(--blue);font-weight:700;font-size:14px;line-height:1.1;margin-top:6px}
.logo .by{font-size:6.5px;color:#333;margin-top:auto;margin-bottom:4px}
.hero{left:132px;top:135px;width:795px;height:363px;border-radius:0 0 8px 8px;
  background:linear-gradient(180deg,#3a3a5a 0,#8a6a6a 35%,#e08a3a 55%,#402030 75%,#140810 100%)}
.arrow{top:285px;width:14px;height:22px}
.thumbs{left:160px;top:433px;display:flex;gap:9px;align-items:flex-end}
.thumb{width:94px;height:56px;border:2px solid var(--yellow);border-radius:4px}
.thumb.active{width:125px;height:72px;margin-bottom:2px}
.sec-title{font-size:15px;font-weight:400;color:var(--heading);display:flex;align-items:center;gap:8px;border-bottom:1px solid var(--line);padding-bottom:5px;width:473px}
.dot{width:12px;height:12px;border-radius:50%;background:var(--bullet);margin:0 2px}
.welcome{left:161px;top:536px}
.welcome p{font-size:10.3px;line-height:15px;letter-spacing:.35px;width:475px;margin-top:10px}
.more{font-size:9px;color:#222;display:flex;align-items:center;gap:4px}
.more i{width:13px;height:13px;border-radius:50%;background:#111;display:inline-flex;align-items:center;justify-content:center}
.offers-title{left:161px;top:702px}
.offers{left:164px;top:738px;width:463px;height:191px;border:1px solid #e4e4e4;background:linear-gradient(180deg,#f0f0f0,#fff 40%)}
.offer{top:13px;width:182px;height:163px;border:5px solid var(--yellow);display:flex;flex-direction:column;justify-content:flex-end;align-items:flex-end;padding:6px;font-family:'Roboto Condensed',sans-serif;font-weight:700;line-height:1}
.offer.spa{left:30px;background:linear-gradient(135deg,#8a5a40,#d8a888 50%,#5a4a40)}
.offer.shop{left:253px;background:linear-gradient(135deg,#dcd4cc,#a04a6a 50%,#eae4de)}
.offer .tag{background:rgba(255,255,255,.8);padding:4px 6px;text-align:right}
.side-arrow{top:818px;width:18px;height:40px;background:#222;display:flex;align-items:center;justify-content:center}
.newsletter{left:160px;top:946px;display:flex;height:29px}
.newsletter .label{background:#333;color:var(--white);font-size:10px;font-weight:700;letter-spacing:.5px;width:101px;display:flex;align-items:center;justify-content:center}
.newsletter .field{width:305px;border:1px solid #ccc;background:linear-gradient(#fff,#eee);font-size:10.5px;color:#999;display:flex;align-items:center;padding-left:11px}
.newsletter .btn{margin-left:5px;width:65px;background:#999;color:var(--white);font-size:11px;display:flex;align-items:center;justify-content:center}
.widget-head{left:674px;width:230px;height:31px;background:var(--yellow);font-size:12px;font-weight:700;color:#6a5500;display:flex;align-items:center;padding-left:18px;letter-spacing:.3px}
.widget{left:681px;width:215px;background:var(--white);box-shadow:0 3px 5px rgba(0,0,0,.18);border-radius:0 0 6px 6px}
.month{font-family:'Roboto Condensed',sans-serif;font-size:15px;color:#444;padding:10px 8px 0;display:flex;justify-content:space-between;align-items:center}
.cal{margin:5px 6px 0;width:203px;border-collapse:collapse;font-family:'Roboto',sans-serif;font-size:9.5px;color:#444}
.cal th{background:#999;color:var(--white);font-size:8px;font-weight:500;height:20px}
.cal td{border:1px solid #ddd;text-align:center;height:21px}
.cal td.today{color:var(--red);font-weight:700}
.book{float:right;margin:7px 8px 8px;background:var(--yellow);border:1px solid var(--yellow-dark);border-radius:3px;font-size:9px;padding:3px 4px;color:#333}
.review{font-size:10px;line-height:15px;letter-spacing:.6px;padding:8px 10px 0 42px;position:relative}
.review .q{position:absolute;left:14px;top:2px;font-size:36px;color:#ccc;font-family:Georgia,serif;line-height:1}
.review .qc{color:#ccc;font-family:Georgia,serif;font-size:22px;line-height:0;vertical-align:-8px;margin-left:3px}
.follow{left:680px;top:953px;display:flex;align-items:center;gap:7px;font-size:13px;color:#444}
.follow .gap{width:8px}
.soc{width:26px;height:26px;border-radius:5px;background:#8a8a8a}
.rule{left:160px;top:1005px;width:744px;height:1px;background:var(--line)}
.f-title{font-family:'Roboto Condensed',sans-serif;font-weight:700;color:var(--red);font-size:15px}
.links{left:161px;top:1025px}
.links ul{list-style:none;display:grid;grid-template-columns:105px 100px;row-gap:13px;margin-top:12px;font-size:10.5px;color:#444}
.links li{display:flex;align-items:center;gap:7px}
.vr{top:1030px;width:1px;height:115px;background:linear-gradient(transparent,#e66,transparent)}
.partners{left:396px;top:1025px;width:175px;font-family:'Roboto',sans-serif}
.partners .intro{font-size:8.5px;line-height:10px;color:#555;margin-top:10px}
.partners ul{list-style:none;font-family:'Bitter',serif;font-size:8.5px;line-height:10px;color:#222;margin-top:8px}
.contact{left:594px;top:1025px}
.map{left:594px;top:1056px;width:119px;height:95px;background:linear-gradient(135deg,#d8e6c0,#eeeade 50%,#cddcb6)}
.c-list{left:734px;top:1053px;font-family:'Roboto',sans-serif;font-size:10.5px;color:#555;list-style:none}
.c-list li{display:flex;gap:10px;margin-bottom:9px;line-height:14px}
.c-list svg{flex:none;margin-top:1px}
.copy{left:0;top:1176px;width:1059px;text-align:center;color:var(--white);font-family:'Roboto',sans-serif;font-size:11px}
</style>
</head>
<body>

<div class="abs topbar">
  <div class="translate">Translate to : <span class="lang"><span class="flag"></span>English<span class="caret"></span></span></div>
  <div class="phone"><svg width="18" height="18" viewBox="0 0 18 18"><circle cx="9" cy="9" r="8" fill="none" stroke="#fff" stroke-width="1.3"/><path d="M6 5l2 2-1 1c.6 1.3 1.7 2.4 3 3l1-1 2 2-1.5 1.5C8 13 5 10 4.5 6.5z" fill="#fff"/></svg>+ 44 (0) 20 7946 0321</div>
  <div class="email"><svg width="17" height="11" viewBox="0 0 17 11"><rect x="1" y="1" width="15" height="9" fill="none" stroke="#fff" stroke-width="1.3"/><path d="M1 1l7.5 5L16 1" fill="none" stroke="#fff" stroke-width="1.3"/></svg>STAY@RESTWELLMARLOW.CO.UK</div>
</div>

<div class="abs panel"></div>

<nav class="abs nav">
  <div class="home"><svg width="20" height="16" viewBox="0 0 20 16"><path d="M10 1L1 8h3v7h5v-4h2v4h5V8h3z" fill="#333"/></svg></div>
  <div class="left"><a>Our Rooms</a><a>Attractions</a><a>London Events</a></div>
  <div class="right"><a>Special Offers</a><a>Photos</a><a>Directions</a><a>Contact</a></div>
</nav>

<div class="abs logo">
  <div class="loc">LONDON - VICTORIA</div>
  <div class="square"></div>
  <div class="name">Restwell Inn</div>
  <div class="by">BY LARKFIELD HOTELS</div>
</div>

<div class="abs hero" role="img" aria-label="Evening view of the river with a lit observation wheel and Westminster skyline"></div>
<svg class="abs arrow" style="left:160px" viewBox="0 0 14 22"><path d="M11 2L3 11l8 9" fill="none" stroke="#ffe21a" stroke-width="4"/></svg>
<svg class="abs arrow" style="left:878px" viewBox="0 0 14 22"><path d="M3 2l8 9-8 9" fill="none" stroke="#ffe21a" stroke-width="4"/></svg>

<div class="abs thumbs">
  <div class="thumb" role="img" aria-label="Double bedroom" style="background:linear-gradient(135deg,#f3e8d8,#c0282a)"></div>
  <div class="thumb" role="img" aria-label="Breakfast counter" style="background:linear-gradient(135deg,#8a7a6a,#d8d0c4)"></div>
  <div class="thumb" role="img" aria-label="Kitchenette" style="background:linear-gradient(135deg,#b89060,#f0ece4)"></div>
  <div class="thumb active" role="img" aria-label="Riverside skyline at night" style="background:linear-gradient(180deg,#5a4a70,#e0903a 55%,#201020)"></div>
  <div class="thumb" role="img" aria-label="Dining room" style="background:linear-gradient(135deg,#f0e0c0,#a05020)"></div>
  <div class="thumb" role="img" aria-label="Bathroom" style="background:linear-gradient(135deg,#eef0f2,#b8c0c8)"></div>
  <div class="thumb" role="img" aria-label="Family room" style="background:linear-gradient(135deg,#f0e4c8,#3050a0 60%,#c03030)"></div>
</div>

<section class="abs welcome">
  <h2 class="sec-title"><span class="dot"></span>Welcome To Restwell Inn</h2>
  <p>Lorem ipsum dolor sit amet, consectetuer adipiscing elit, sed diam nonummy nibh euismod tincidunt ut laoreet dolore magna aliquam erat volutpat. Ut wisi enim ad minim veniam, quis nostrud exerci tation ullamcorper suscipit lobortis nisl ut aliquip. Lorem ipsum dolor sit amet, consectetuer adipiscing elit, sed diam nonummy nibh euismod tincidunt ut laoreet dolore magna aliquam erat volutpat. Ut wisi enim ad minim veniam, quis nostrud exerci tation ullamcorper suscipit lobortis nisl ut aliquip.</p>
  <div class="more" style="justify-content:flex-end;margin-top:6px"><i><svg width="6" height="8"><path d="M1 1l4 3-4 3" fill="none" stroke="#ffe21a" stroke-width="1.6"/></svg></i>Read more</div>
</section>

<h2 class="abs sec-title offers-title"><span class="dot"></span>Our Special Offers</h2>
<div class="abs offers">
  <div class="abs offer spa" role="img" aria-label="Spa foot treatment">
    <div class="tag"><div style="color:var(--red);font-size:26px">SPA</div><div style="color:#222;font-size:16px;font-weight:400">TREATMENT</div><div style="color:#222;font-size:16px">Save <span style="color:var(--red);font-size:28px">25%</span></div></div>
  </div>
  <div class="abs offer shop" role="img" aria-label="Shopping for handbags">
    <div class="tag"><div style="color:var(--red);font-size:22px">Shopping</div><div style="color:#222;font-size:16px;font-weight:400;text-align:center">IN</div><div style="color:var(--blue);font-size:28px">LONDON</div></div>
  </div>
</div>
<div class="abs side-arrow" style="left:160px;border-radius:0 20px 20px 0"><svg width="8" height="12"><path d="M6 1L2 6l4 5" fill="none" stroke="#ffe21a" stroke-width="2"/></svg></div>
<div class="abs side-arrow" style="left:613px;border-radius:20px 0 0 20px"><svg width="8" height="12"><path d="M2 1l4 5-4 5" fill="none" stroke="#fff" stroke-width="2"/></svg></div>

<form class="abs newsletter">
  <div class="label">NEWSLETTER</div>
  <div class="field">E-mail address</div>
  <div class="btn">Subscribe</div>
</form>

<div class="abs widget-head" style="top:532px">BOOKING CALENDAR</div>
<div class="abs widget" style="top:563px;height:191px">
  <div class="month">November 2013 <svg width="13" height="13"><circle cx="6.5" cy="6.5" r="6.5" fill="#eee"/><path d="M5 3.5l3 3-3 3" fill="none" stroke="#222" stroke-width="1.6"/></svg></div>
  <table class="cal">
    <tr><th>MON</th><th>TUE</th><th>WED</th><th>THU</th><th>FRI</th><th>SAT</th><th>SUN</th></tr>
    <tr><td>1</td><td>2</td><td>3</td><td>4</td><td>5</td><td>6</td><td>7</td></tr>
    <tr><td>8</td><td>9</td><td>10</td><td>11</td><td>12</td><td>13</td><td>14</td></tr>
    <tr><td>15</td><td>16</td><td>17</td><td>18</td><td>19</td><td>20</td><td class="today">21</td></tr>
    <tr><td>22</td><td>23</td><td>24</td><td>25</td><td>26</td><td>27</td><td>28</td></tr>
    <tr><td>29</td><td>30</td><td colspan="5"></td></tr>
  </table>
  <div class="book">Click To Book</div>
</div>

<div class="abs widget-head" style="top:776px;padding-left:22px">
  JOURNEYSCOPE REVIEWS
  <svg width="30" height="10" style="margin-left:auto;margin-right:10px"><path d="M0 5l5-4v3h7v2H5v3zM30 5l-5-4v3h-7v2h7v3z" fill="#222"/></svg>
</div>
<div class="abs widget" style="top:807px;height:122px">
  <div class="review"><span class="q">&ldquo;</span>Lorem ipsum dolor sit amet, adipiscing elit. Mauris felis ante,semper et, accumsan quis diam.tincidunt felis nec magna feugiat ulla atvesti bulum.<span class="qc">&rdquo;</span></div>
  <div class="more" style="justify-content:flex-end;margin:10px 10px 0 0"><i><svg width="6" height="8"><path d="M1 1l4 3-4 3" fill="none" stroke="#ffe21a" stroke-width="1.6"/></svg></i>Read more</div>
</div>

<div class="abs follow">Follow Us<span class="gap"></span><span class="soc"></span><span class="soc"></span><span class="soc"></span><span class="soc"></span></div>

<div class="abs rule"></div>

<div class="abs links">
  <h3 class="f-title">Quick Links</h3>
  <ul>
    <li><svg width="11" height="9"><path d="M0 3h5V0l6 4.5L5 9V6H0z" fill="#f5c400"/></svg>Home</li>
    <li><svg width="11" height="9"><path d="M0 3h5V0l6 4.5L5 9V6H0z" fill="#f5c400"/></svg>Special Offers</li>
    <li><svg width="11" height="9"><path d="M0 3h5V0l6 4.5L5 9V6H0z" fill="#f5c400"/></svg>Our Rooms</li>
    <li><svg width="11" height="9"><path d="M0 3h5V0l6 4.5L5 9V6H0z" fill="#f5c400"/></svg>Photos</li>
    <li><svg width="11" height="9"><path d="M0 3h5V0l6 4.5L5 9V6H0z" fill="#f5c400"/></svg>Attractions</li>
    <li><svg width="11" height="9"><path d="M0 3h5V0l6 4.5L5 9V6H0z" fill="#f5c400"/></svg>Direction</li>
    <li><svg width="11" height="9"><path d="M0 3h5V0l6 4.5L5 9V6H0z" fill="#f5c400"/></svg>London Events</li>
    <li><svg width="11" height="9"><path d="M0 3h5V0l6 4.5L5 9V6H0z" fill="#f5c400"/></svg>Contact Us</li>
  </ul>
</div>
<div class="abs vr" style="left:380px"></div>

<div class="abs partners">
  <h3 class="f-title">Partner Hotels</h3>
  <p class="intro">This hotel is owned and operated by the Harrowgate Hotel Group, please take a look of some of our other hotels below:</p>
  <ul>
    <li>Canalside House - Camden</li>
    <li>Westway Lodge - Earls Court</li>
    <li>Middlegate Hotel</li>
    <li>Pocket Rooms Victoria</li>
    <li>Pocket Rooms Paddington</li>
    <li>Restwell Suites - King's Cross</li>
  </ul>
</div>
<div class="abs vr" style="left:577px"></div>

<h3 class="abs f-title contact">Contact Info</h3>
<div class="abs map" role="img" aria-label="Street map around the hotel"></div>
<ul class="abs c-list">
  <li><svg width="10" height="13"><path d="M5 0a4.5 4.5 0 0 0-4.5 4.5C.5 8 5 13 5 13s4.5-5 4.5-8.5A4.5 4.5 0 0 0 5 0z" fill="#2a6ab0"/><circle cx="5" cy="4.5" r="1.6" fill="#fff"/></svg><span>42-48 Alder Row, Victoria<br>London SW1 9ZX</span></li>
  <li><svg width="12" height="12"><path d="M2 0l3 3-1.5 1.5c.8 1.6 2.4 3.2 4 4L9 7l3 3-2 2C5 11.5.5 7 0 2z" fill="#2a6ab0"/></svg><span>+ 44 (0) 20 7946 0321</span></li>
  <li><svg width="13" height="11"><rect x="1" y="3" width="11" height="7" rx="1" fill="#2a6ab0"/><rect x="3" y="0" width="7" height="3" fill="#2a6ab0"/><rect x="4" y="5" width="5" height="3" fill="#fff"/></svg><span>+ 44 (0) 20 7946 0874</span></li>
  <li><svg width="13" height="10"><rect width="13" height="10" fill="#2a6ab0"/><path d="M0 0l6.5 5L13 0" fill="none" stroke="#fff"/></svg><span>stay@restwellmarlow.co.uk</span></li>
</ul>

<footer class="abs copy">© 2013 RestwellINN &nbsp;|&nbsp; All Rights Reserved</footer>

</body>
</html>
```